Web landing page design

- Create a Web Design (Uncoded - PSD layout only)

We need a single web page design to promote our service. This page will
acts as a landing page for users and also be utilized in social media
advertising. Please provide us with a cutting edge design. I have attached
a link for what the company is about. In essence we are a photo checking
service which reviews photos for retailers, hotels abd car dealerships to
check everything is good after a service has been performed. Whether it be
a new promotion, cleaning or just checking prices. I am looking for a
design to say that we do many photos and at a very cost effective price
(team based in Mexico)

Link: https://slidora.example/view/kq3Fz8wPnT2dXr7HsLmV/
*Deadline*
5 days
*Updates*

- The Start Here box needs to look like this:

-Start Here (heading)
-A box for email addresses to be entered
-Then a check box with "Yes, I have read and agree to the Privacy Policy
and agree to receive email marketing from Tallumo38'
-A submit button

All of this information needs to be in one box please. And please feel
free to contact me if you have any questions about this.

*Target Market(s)*
Retail business, Merchandising companies, Rental property owners, Car
dealers
Updates

Please can you submit entries. I am just looking for a tidy to a presentation already created. Just needs design touches.

Target Market(s)

Ability for audience to understand concept quickly
Benefits to why to use the product stand out
Technology driven approach

Industry/Entity Type

Retail

Number of Pages Required

1 page

Colors
0792cd

Requirements
Must have
• Clean and modern design

```html
<!DOCTYPE html>
<html lang="en">
<head>
<meta charset="utf-8">
<title>Start Here – Landing Page</title>
<link rel="stylesheet" href="https://fonts.googleapis.com/css2?family=Exo+2:wght@400;600;700&family=Lato:ital,wght@0,400;0,700;1,400&display=swap">
<style>
  :root {
    --brand-blue: #2f7cf6;
    --accent-cyan: #0792cd;
    --button-cyan: #13b3e0;
    --teal: #1fd6b0;
    --mint: #3fe8c8;
    --panel-navy: #13304a;
    --panel-deep: #0c2236;
    --chrome-grey: #e6e8eb;
    --chrome-line: #d2d5da;
    --text-dark: #3a3f47;
    --text-muted: #6b7079;
    --nav-grey: #5d6269;
    --track: #cfeaf4;
    --white: #ffffff;
  }
  * { box-sizing: border-box; margin: 0; padding: 0; }
  html, body { width: 1200px; height: 920px; overflow: hidden; background: var(--white); }
  body { font-family: "Lato", sans-serif; color: var(--text-dark); position: relative; }

  .browser-bar {
    position: absolute; left: 0; top: 0; width: 1200px; height: 52px;
    background: var(--chrome-grey); border-bottom: 1px solid var(--chrome-line);
    display: flex; align-items: center; padding: 0 16px; gap: 10px;
  }
  .window-dot { width: 12px; height: 12px; border-radius: 50%; }
  .window-dot.close { background: #fc5f57; }
  .window-dot.minimise { background: #fdbc2e; }
  .window-dot.zoom { background: #28c840; }
  .nav-arrows { display: flex; margin-left: 12px; border: 1px solid var(--chrome-line); border-radius: 4px; background: var(--white); }
  .nav-arrows span { width: 22px; height: 22px; display: flex; align-items: center; justify-content: center; }
  .nav-arrows span + span { border-left: 1px solid var(--chrome-line); }
  .address-field {
    flex: 1; height: 26px; border-radius: 13px; background: var(--white);
    border: 1px solid var(--chrome-line); font-size: 11px; font-style: italic;
    color: var(--text-dark); display: flex; align-items: center; padding: 0 14px;
  }

  .site-header {
    position: absolute; left: 0; top: 52px; width: 1200px; height: 78px;
    display: flex; align-items: center; padding: 0 40px;
  }
  .site-brand { display: flex; align-items: center; gap: 8px; font-size: 19px; color: var(--brand-blue); }
  .site-brand .brand-dot { width: 18px; height: 18px; border-radius: 50%; background: var(--brand-blue); }
  .site-nav { margin-left: auto; display: flex; align-items: center; gap: 30px; font-size: 14px; font-style: italic; color: var(--nav-grey); }
  .demo-button {
    margin-left: 6px; background: var(--brand-blue); color: var(--white); font-style: normal;
    padding: 9px 22px; border-radius: 18px; font-size: 14px;
  }

  .presentation {
    position: absolute; left: 60px; top: 140px; width: 1080px; height: 520px;
    border-radius: 24px; overflow: hidden; background: var(--panel-navy);
  }
  .presentation-backdrop {
    position: absolute; inset: 0;
    background: radial-gradient(ellipse at 60% 45%, #1c4565 0%, var(--panel-navy) 45%, var(--panel-deep) 100%);
  }
  .deck-brand {
    position: absolute; left: 30px; top: 30px; display: flex; align-items: center; gap: 10px;
    font-family: "Exo 2", sans-serif; font-size: 26px; font-weight: 400; color: var(--white);
  }
  .deck-brand .brand-square { width: 18px; height: 18px; border: 2px solid var(--white); }

  .signup-card {
    position: absolute; left: 330px; top: 72px; width: 420px; height: 340px;
    background: var(--white); border-radius: 14px; overflow: hidden;
    box-shadow: 0 16px 36px rgba(0,0,0,0.35);
    font-family: "Exo 2", sans-serif;
  }
  .card-head {
    height: 128px; background: linear-gradient(180deg, var(--mint) 0%, var(--teal) 100%);
    display: flex; align-items: center; padding: 0 24px; gap: 20px; color: var(--white);
  }
  .card-head svg { flex: none; }
  .card-title { font-size: 36px; font-weight: 700; line-height: 1.1; text-align: center; }
  .card-intro { font-size: 12px; text-align: center; margin-top: 8px; line-height: 1.4; font-style: italic; }
  .card-body { padding: 22px 28px; }
  .email-field {
    border-bottom: 1px solid #9aa0a8; text-align: center; padding: 8px 0 14px;
    font-size: 15px; color: var(--text-muted);
  }
  .consent { display: flex; gap: 10px; margin-top: 18px; font-size: 12px; line-height: 1.5; color: var(--text-dark); }
  .consent .tick-box { flex: none; width: 13px; height: 13px; border: 1.5px solid #555; border-radius: 50%; margin-top: 2px; }
  .consent a { color: var(--accent-cyan); text-decoration: none; }
  .submit-button {
    margin-top: 18px; height: 48px; border-radius: 24px;
    background: linear-gradient(180deg, #27c3ec 0%, var(--button-cyan) 100%);
    color: var(--white); font-size: 19px; font-weight: 600;
    display: flex; align-items: center; justify-content: center; position: relative;
    box-shadow: 0 4px 10px rgba(7,146,205,0.35);
  }
  .submit-button svg { position: absolute; right: 10px; top: 9px; }

  .deck-progress { position: absolute; left: 60px; top: 684px; width: 1080px; height: 5px; border-radius: 3px; background: var(--track); }
  .deck-progress .done { width: 60px; height: 5px; border-radius: 3px; background: var(--accent-cyan); }
  .deck-back { position: absolute; left: 60px; top: 706px; }
  .deck-arrows { position: absolute; left: 540px; top: 740px; display: flex; gap: 36px; }
  .deck-arrows span { width: 32px; height: 32px; border-radius: 50%; background: #6f7780; display: flex; align-items: center; justify-content: center; }
  .deck-fullscreen { position: absolute; left: 1104px; top: 790px; width: 32px; height: 32px; border-radius: 4px; background: #7c858f; display: flex; align-items: center; justify-content: center; }
</style>
</head>
<body>
  <div class="browser-bar">
    <span class="window-dot close"></span>
    <span class="window-dot minimise"></span>
    <span class="window-dot zoom"></span>
    <div class="nav-arrows">
      <span><svg width="8" height="12" viewBox="0 0 8 12"><path d="M6 1 1 6l5 5" fill="none" stroke="#777" stroke-width="1.5"/></svg></span>
      <span><svg width="8" height="12" viewBox="0 0 8 12"><path d="M2 1l5 5-5 5" fill="none" stroke="#777" stroke-width="1.5"/></svg></span>
    </div>
    <div class="address-field">https://slidora.example/view/kq3Fz8wPnT2dXr7HsLmV/</div>
  </div>

  <header class="site-header">
    <div class="site-brand"><span class="brand-dot"></span>Slidora Business</div>
    <nav class="site-nav">
      <span>Conversations</span>
      <span>Customers</span>
      <span>Workshop</span>
      <span>Support</span>
      <span>Log in</span>
      <span class="demo-button">Request a Demo</span>
    </nav>
  </header>

  <main class="presentation">
    <div class="presentation-backdrop" role="img" aria-label="Dark blue collage of store, hotel and car dealership photos behind the slide"></div>
    <div class="deck-brand"><span class="brand-square"></span>Vistelo</div>

    <section class="signup-card">
      <div class="card-head">
        <svg width="70" height="62" viewBox="0 0 70 62" aria-hidden="true">
          <rect x="4" y="4" width="36" height="46" rx="4" fill="#fff"/>
          <rect x="11" y="16" width="20" height="3" fill="#9fe8da"/>
          <rect x="11" y="24" width="16" height="3" fill="#9fe8da"/>
          <rect x="24" y="28" width="42" height="30" rx="4" fill="#f4fbf9"/>
          <path d="M26 31l19 14 19-14" fill="none" stroke="#9fe8da" stroke-width="2.5"/>
        </svg>
        <div>
          <h1 class="card-title">Start here</h1>
          <p class="card-intro">Lorem Ipsum is simply dummy text<br>of the printing and typesetting industry.</p>
        </div>
      </div>
      <div class="card-body">
        <div class="email-field">enter email address</div>
        <label class="consent">
          <span class="tick-box"></span>
          <span>I have read and agree to the <a>Privacy Policy</a> and agree to receive email marketing from <a>Tallumo38</a></span>
        </label>
        <div class="submit-button">Submit
          <svg width="30" height="30" viewBox="0 0 30 30" aria-hidden="true"><circle cx="15" cy="15" r="15" fill="#fff"/><path d="M9 15.5l4 4 8-9" fill="none" stroke="#13b3e0" stroke-width="3" stroke-linecap="round" stroke-linejoin="round"/></svg>
        </div>
      </div>
    </section>
  </main>

  <div class="deck-progress"><div class="done"></div></div>
  <svg class="deck-back" width="22" height="22" viewBox="0 0 22 22" aria-label="Back"><path d="M9 3 2 9l7 6V11c6 0 9 2 11 8 0-7-4-12-11-12z" fill="#6f7780"/></svg>
  <div class="deck-arrows">
    <span><svg width="14" height="14" viewBox="0 0 14 14"><path d="M13 7H2M6 2 1 7l5 5" fill="none" stroke="#fff" stroke-width="2"/></svg></span>
    <span><svg width="14" height="14" viewBox="0 0 14 14"><path d="M1 7h11M8 2l5 5-5 5" fill="none" stroke="#fff" stroke-width="2"/></svg></span>
  </div>
  <div class="deck-fullscreen"><svg width="18" height="18" viewBox="0 0 18 18"><path d="M11 2h5v5M16 2l-6 6M7 16H2v-5M2 16l6-6" fill="none" stroke="#fff" stroke-width="1.8"/></svg></div>
</body>
</html>
```